Bicycle Tour Schedule on a Business Card

Need to develop a 2 side business card that highlights a series of bike tours on 1 side and a series of events on the other side.
This will be inserted into a card wallet that attaches to a cell phone and will be handed out at an expo. The card wallets are black and red so color must coordinate with both. There is a photo of the card wallets attached.

1 side needs to be devoted to Pedal Vista Rides and the others to KRV Partners events on the other. Dates and websites are very important.

Target Market(s)

Cyclists
Predominantly men ages 40+
Educated, Professionals

Industry/Entity Type

Business

Font styles to use
Serif

Requirements
Must have
• Pedal vista rides logo on 1 side and KRV Partners logo on the other side
• dates and websites clearly visible
• Design of both sides must go together.
• Must be portrait not landscape

```html
<!DOCTYPE html>
<html lang="en">
<head>
<meta charset="utf-8">
<title>Pedal Vista Rides &amp; KRV Partners – Event Cards</title>
<link rel="stylesheet" href="https://fonts.googleapis.com/css2?family=Open+Sans:ital,wght@0,400;0,600;0,700;1,700&display=swap">
<style>
  :root {
    --backdrop: #8f9090;
    --card: #ececec;
    --ink: #3a3a3a;
    --tour-blue: #0c5aa6;
    --tour-green: #3aa14a;
    --event-red: #c8102e;
    --white: #ffffff;
  }
  * { box-sizing: border-box; margin: 0; padding: 0; }
  html, body {
    width: 1105px;
    height: 1200px;
    overflow: hidden;
    background: var(--backdrop);
    font-family: "Open Sans", Arial, sans-serif;
    color: var(--ink);
  }
  .sheet { position: relative; width: 1105px; height: 1200px; }
  .card {
    position: absolute;
    top: 269px;
    width: 398px;
    height: 698px;
    background: var(--card);
    text-align: center;
  }
  .card--tours { left: 113px; }
  .card--events { left: 597px; }

  .brand {
    position: absolute;
    left: 0; right: 0;
    display: flex;
    align-items: center;
    justify-content: center;
    gap: 14px;
    font-weight: 700;
  }
  .card--tours .brand {
    top: 60px; height: 100px;
    color: var(--tour-green);
    font-size: 34px;
  }
  .card--events .brand {
    top: 30px; height: 170px;
    flex-direction: column;
    gap: 16px;
    color: var(--event-red);
    font-size: 32px;
  }
  .brand__mark {
    width: 96px; height: 96px;
    background: var(--event-red);
  }

  .band {
    position: absolute;
    left: 0; right: 0;
    display: flex;
    align-items: center;
    justify-content: center;
    color: var(--white);
    font-weight: 700;
    font-style: italic;
    font-size: 20px;
    line-height: 24px;
  }
  .band--tours { top: 231px; height: 102px; background: var(--tour-blue); }
  .band--events { top: 238px; height: 60px; background: var(--event-red); }

  .schedule {
    position: absolute;
    left: 0; right: 0;
    list-style: none;
    display: flex;
    flex-direction: column;
  }
  .schedule--tours { top: 369px; gap: 18px; font-size: 18px; line-height: 25px; }
  .schedule--events { top: 314px; gap: 12px; font-size: 17.5px; line-height: 23px; }
  .event__name { font-weight: 400; }
  .event__date, .event__site { font-weight: 700; }
</style>
</head>
<body>
<main class="sheet">
  <section class="card card--tours" aria-label="Pedal Vista Rides tour schedule">
    <div class="brand">Pedal Vista Rides</div>
    <div class="band band--tours">Fully supported bike tours.<br>Discover the hidden gems on<br>two wheels</div>
    <ul class="schedule schedule--tours">
      <li class="event">
        <div class="event__name">Heart of Colorado</div>
        <div class="event__date">June 26 - July 2, 2016</div>
      </li>
      <li class="event">
        <div class="event__name">Colorado Front Range Tour</div>
        <div class="event__date">August 14-20, 2016</div>
      </li>
      <li class="event">
        <div class="event__name">Cape Cod Tour</div>
        <div class="event__date">October 9 -15, 2016</div>
      </li>
      <li class="event">
        <div class="event__name">Florida Key Tours</div>
        <div class="event__date">November 6-12, 2016 &amp;<br>December 4-10, 2016</div>
      </li>
    </ul>
  </section>

  <section class="card card--events" aria-label="KRV Partners event schedule">
    <div class="brand"><span class="brand__mark" aria-hidden="true"></span>KRV Partners</div>
    <div class="band band--events">Trio Wheel Series:<br>Cycling camps for youth</div>
    <ul class="schedule schedule--events">
      <li class="event">
        <div class="event__name">Mountain Bike Camp</div>
        <div class="event__date">July 8-10, 2016</div>
      </li>
      <li class="event">
        <div class="event__name">Cyclocross Camp</div>
        <div class="event__date">August 26-28, 2016</div>
        <div class="event__site">Triowheelseries.org</div>
      </li>
      <li class="event">
        <div class="event__name">Mile High Hundred Ride</div>
        <div class="event__date">June 18, 2016</div>
        <div class="event__site">Milehighhundred.com</div>
      </li>
      <li class="event">
        <div class="event__name">Ridgeline Park Loop Challenge</div>
        <div class="event__date">July 30, 2016 - Ridgelineloop.com</div>
      </li>
      <li class="event">
        <div class="event__name">Jolly Spoke Ride</div>
        <div class="event__date">September 11, 2016</div>
        <div class="event__site">jollyspokeride.com</div>
      </li>
    </ul>
  </section>
</main>
</body>
</html>
```